New Business Card Design Project

Hi there

Could you please make a design that is soft and appealing to people who would purchase gemstones, buy healing jewellery, seek counselling, may seek energy healing and/or learn English. Essentially I'm looking for something with a soft human design. Please incorporate the logo and select font that can be easily read and softer images in the background - but not too busy. I would like it double sided as well.

Optional: Elements could include gemstones, feathers, plants and images that are happy and calming.

Target Market(s)

People into alternative health, those from non-English speaking backgrounds, businesses

Contact Information for Business Card

Leo Marsdon
Mobile: 0412 586 239, Facebook and Instagram Logos,
ABN: 51 742 118 603 (Australian Business Number - small at the bottom)

Requirements
Must have
• My project must have:
- Tranquil Harbor logo
- Symbols that represent the 4 main services: 1. Gemstones/jewellery, 2. counselling, 3. meditation/energy healing, 4. education
Nice to have
• Clear and easy to read.

```html
<!DOCTYPE html>
<html lang="en">
<head>
<meta charset="utf-8">
<title>Tranquil Harbor – Business Card</title>
<link rel="stylesheet" href="https://fonts.googleapis.com/css2?family=Montserrat:wght@400;500;600&family=Open+Sans:wght@400;600&display=swap">
<style>
  :root {
    --stage: #2b2d30;
    --card-white: #ffffff;
    --teal: #2ba597;
    --teal-deep: #1f8f83;
    --green: #5aa83a;
    --ink: #3a3a3a;
    --rule: #1a1a1a;
  }
  * { box-sizing: border-box; margin: 0; padding: 0; }
  html, body { width: 1200px; height: 898px; overflow: hidden; }
  body {
    background: var(--stage);
    position: relative;
    font-family: "Open Sans", sans-serif;
  }
  .card {
    position: absolute;
    left: 250px;
    width: 700px;
    height: 400px;
    border-radius: 28px;
    overflow: hidden;
  }
  .card--front { top: 29px; background: var(--card-white); }
  .card--back { top: 469px; background: var(--teal); }

  .front__glow {
    position: absolute;
    left: -60px; top: -80px;
    width: 380px; height: 380px;
    border-radius: 50%;
    background: radial-gradient(circle, rgba(43,165,151,0.16) 0%, rgba(43,165,151,0.06) 55%, rgba(43,165,151,0) 72%);
  }
  .contact { position: absolute; left: 60px; top: 92px; }
  .contact__name {
    font-family: "Montserrat", sans-serif;
    font-weight: 500;
    font-size: 30px;
    color: var(--teal);
    margin-bottom: 12px;
  }
  .contact__line {
    display: flex; align-items: center; gap: 10px;
    font-size: 16px; color: var(--ink); line-height: 26px;
  }
  .contact__icon { width: 14px; height: 14px; }
  .contact__line--plain { padding-left: 24px; }
  .brand {
    position: absolute;
    left: 330px; top: 112px;
    display: flex; align-items: center; gap: 16px;
  }
  .brand__mark {
    flex: none;
    width: 46px; height: 46px; border-radius: 50%;
    background: var(--teal);
  }
  .brand__name {
    font-family: "Montserrat", sans-serif;
    font-weight: 600;
    font-size: 32px;
    line-height: 40px;
    letter-spacing: 1px;
    color: var(--teal);
  }
  .front__rule {
    position: absolute;
    left: 300px; top: 232px;
    width: 360px; height: 2px;
    background: var(--rule);
  }
  .abn {
    position: absolute;
    right: 46px; bottom: 40px;
    font-size: 16px; color: var(--ink); letter-spacing: 0.5px;
  }
  .abn__label { color: var(--green); margin-right: 6px; }

  .back__art { position: absolute; inset: 0; width: 700px; height: 400px; }
  .service-label {
    font-family: "Montserrat", sans-serif;
    font-size: 13px;
    letter-spacing: 1.2px;
    fill: #ffffff;
  }
</style>
</head>
<body>

<section class="card card--front">
  <div class="front__glow" role="img" aria-label="Faint brand symbol decoration"></div>
  <div class="contact">
    <p class="contact__name">Leo Marsdon</p>
    <p class="contact__line">
      <svg class="contact__icon" viewBox="0 0 24 24" aria-hidden="true"><rect x="6" y="2" width="12" height="20" rx="2" fill="#5aa83a"/><rect x="8" y="5" width="8" height="12" fill="#fff"/></svg>
      0412 586 239
    </p>
    <p class="contact__line contact__line--plain">hello@example.com</p>
  </div>
  <div class="brand">
    <span class="brand__mark"></span>
    <span class="brand__name">TRANQUIL<br>HARBOR</span>
  </div>
  <div class="front__rule"></div>
  <p class="abn"><span class="abn__label">ABN:</span>51 742 118 603</p>
</section>

<section class="card card--back">
  <svg class="back__art" viewBox="0 0 700 400" aria-label="Services">
    <defs>
      <radialGradient id="softGlow" cx="50%" cy="50%" r="55%">
        <stop offset="0" stop-color="#ffffff" stop-opacity="0.14"/>
        <stop offset="1" stop-color="#ffffff" stop-opacity="0"/>
      </radialGradient>
      <path id="arcLeft" d="M 258.1 291.9 A 130 130 0 0 1 258.1 108.1"/>
      <path id="arcTop" d="M 282.4 55 A 160 160 0 0 1 509.4 213.9"/>
      <path id="arcBottom" d="M 199.6 254.7 A 160 160 0 0 0 500.4 254.7"/>
    </defs>
    <rect width="700" height="400" fill="url(#softGlow)" role="img" aria-label="Soft faint brand symbol decoration"/>

    <text class="service-label" text-anchor="middle">
      <textPath href="#arcLeft" startOffset="50%">COUNSELLING</textPath>
    </text>
    <text class="service-label" text-anchor="middle">
      <textPath href="#arcTop" startOffset="50%">MEDITATION/ENERGY HEALING</textPath>
    </text>
    <text class="service-label" text-anchor="middle">
      <textPath href="#arcBottom" startOffset="50%">GEMSTONES/JEWELLERY</textPath>
    </text>

    <circle cx="285" cy="165" r="24" fill="#ffffff" fill-opacity="0.25" role="img" aria-label="Counselling symbol: head outline with heart"/>
    <circle cx="435" cy="135" r="24" fill="#ffffff" fill-opacity="0.25" role="img" aria-label="Meditation symbol: seated figure with energy points"/>
    <circle cx="428" cy="262" r="22" fill="#c9cdd1" role="img" aria-label="Gemstone photograph"/>

    <g fill="none" stroke="#fff" stroke-width="2.5">
      <path d="M336 172 q8 -6 14 0 v18 q-6 -6 -14 0 z"/>
      <path d="M350 172 q8 -6 14 0 v18 q-8 -6 -14 0"/>
    </g>
    <text x="350" y="212" text-anchor="middle" class="service-label">EDUCATION</text>

    <circle cx="339" cy="232" r="7" fill="#fff"/>
    <rect x="355" y="225" width="14" height="14" rx="3" fill="#fff"/>
  </svg>
</section>

</body>
</html>
```